Business Card Design Project

I am a Chiropractor that is looking for a new business card.  Our logo was slightly changed lately, therefore need a new, more professional look.
We are a modern, non-stuffy chiropractic office.  Want a contemporary look that will let people know this is not your typical doctors office.  Our logo is red, and contains the name of our business: realign.  The u in the logo is green, stressing the most important part of our business: "u"

Target Market(s)
moderate to upper income bracket, family friendly
www.realignspine.example
Gordon Pell
Family Chiropractor
412 Birch Ave
Linwood, TX 78690
512.555.0147 phone
512.555.0148 fax
Industry/Entity Type
Business
Requirements
Must have
- www.realignspine.example
Gordon Pell
Family Chiropractor
412 Birch Ave
Linwood, TX 78690
512.555.0147 phone
512.555.0148 fax

```html
<!DOCTYPE html>
<html lang="en">
<head>
<meta charset="utf-8">
<title>Gordon Pell – Business Card</title>
<link rel="stylesheet" href="https://fonts.googleapis.com/css2?family=Questrial&family=Arimo&display=swap">
<style>
  :root {
    --backdrop: #bcbcbc;
    --card: #f1f1f1;
    --ink: #1a1a1a;
    --ink-soft: #333333;
    --brand-red: #e8403a;
    --rule: #2a2a2a;
  }
  html, body {
    margin: 0;
    padding: 0;
    width: 1200px;
    height: 682px;
    overflow: hidden;
    background: var(--backdrop);
  }
  .canvas {
    position: relative;
    width: 1200px;
    height: 682px;
  }
  .card {
    position: absolute;
    top: 192px;
    width: 498px;
    height: 299px;
    background: var(--card);
    border-radius: 6px;
    overflow: hidden;
  }
  .card--front { left: 68px; }
  .card--back { left: 628px; }

  .divider {
    position: absolute;
    left: 20px;
    right: 20px;
    height: 26px;
  }
  .divider::before {
    content: "";
    position: absolute;
    left: 0; right: 0; top: 0;
    height: 1px;
    background: linear-gradient(90deg, transparent, var(--rule) 30%, var(--rule) 70%, transparent);
  }
  .divider::after {
    content: "";
    position: absolute;
    left: 15%; right: 15%; top: 1px;
    height: 18px;
    background: radial-gradient(ellipse at 50% 0%, rgba(0,0,0,0.22), rgba(0,0,0,0) 70%);
  }

  .person {
    position: absolute;
    top: 72px;
    left: 0; right: 0;
    text-align: center;
  }
  .person__name {
    margin: 0;
    font-family: "Questrial", sans-serif;
    font-weight: 400;
    font-size: 35px;
    line-height: 1;
    color: var(--ink);
  }
  .person__title {
    margin: 10px 0 0;
    font-family: "Arimo", sans-serif;
    font-size: 13px;
    color: var(--ink-soft);
  }
  .card--front .divider { top: 144px; }

  .contact {
    position: absolute;
    top: 172px;
    left: 0; right: 0;
    margin: 0;
    text-align: center;
    font-family: "Arimo", sans-serif;
    font-style: normal;
    font-size: 14.5px;
    line-height: 23px;
    color: var(--ink-soft);
  }
  .contact__address { font-size: 16px; }
  .contact__web {
    font-family: "Questrial", sans-serif;
    font-size: 17px;
    color: var(--ink);
  }

  .brand {
    position: absolute;
    top: 100px;
    left: 0; right: 0;
    display: flex;
    align-items: center;
    justify-content: center;
    gap: 14px;
  }
  .brand__dot {
    width: 22px;
    height: 22px;
    border-radius: 50%;
    background: var(--brand-red);
  }
  .brand__name {
    font-family: "Questrial", sans-serif;
    font-size: 58px;
    line-height: 1;
    color: var(--brand-red);
  }
  .card--back .divider { top: 239px; }
</style>
</head>
<body>
<main class="canvas">
  <section class="card card--front" aria-label="Business card front">
    <div class="person">
      <h1 class="person__name">Gordon Pell</h1>
      <p class="person__title">Family Chiropractor</p>
    </div>
    <div class="divider"></div>
    <address class="contact">
      Phone:. 512.555.0147<br>
      Fax:. 512.555.0148<br>
      <span class="contact__address">412 Birch Ave</span><br>
      <span class="contact__address">Linwood, TX 78690</span><br>
      <span class="contact__web">www.realignspine.example</span>
    </address>
  </section>

  <section class="card card--back" aria-label="Business card back">
    <div class="brand">
      <span class="brand__dot"></span>
      <span class="brand__name">realign</span>
    </div>
    <div class="divider"></div>
  </section>
</main>
</body>
</html>
```